Design a new 2 Blade razor pack for retail sales in Supermarkets

Redesign or update existing new Men's and Ladies Brisk Blades razor packets. Not fussed if you keep the same feel as the old pack. The Pack will be the same plastic pouch, 5 Pack.
The Men's razor will be Silver colour called The Chief (The Packet colour for men should stay similar blue / aqua). and the Ladies razor will be a Purple colour called Bloom Her Way. (Please Change the Ladies colour Packet).
Both razors will have a lubricating Strip. (As Attached). You don't have to use the whole razor.
I have attached the dimensions of the pack.
I have also attached the old pack front and back.
I really would like to keep a clear window of some sort to see the razors.
I have also attached Company details for the back.

Please do mock up of how the Pack will look Front and back.

Target Market(s)

Male and Female shoppers

Industry/Entity Type

Retail

Font styles to use
Sans Serif

Colors

Designer to choose colors to be used in the design.

Requirements
Must have
• A clear view section so you can see the razors.
• Small Logo Brisk Blades on the front and Back.
Nice to have
• A nice modern feel, razor picture being the dominating image.
• Clean Fresh sharp look.
Should not have
• Too many colours not too busy.

```html
<!DOCTYPE html>
<html lang="en">
<head>
<meta charset="utf-8">
<title>Brisk Blades – The Chief 5 Pack</title>
<link rel="stylesheet" href="https://fonts.googleapis.com/css2?family=Orbitron:wght@900&family=Exo+2:ital,wght@0,800;1,800&display=swap">
<style>
  :root {
    --backdrop: #b4501a;
    --aqua: #1ea3bf;
    --aqua-deep: #147f98;
    --aqua-light: #3cc0da;
    --orange: #ee8a16;
    --orange-deep: #c9670b;
    --navy: #1d2a6e;
    --gold: #d9cb1c;
    --silver-hi: #f2f4f5;
    --silver-lo: #b9c0c4;
  }
  html, body {
    margin: 0;
    width: 1200px;
    height: 1200px;
    overflow: hidden;
    background: var(--backdrop);
  }
  .pack {
    position: absolute;
    left: 230px;
    top: 44px;
    width: 740px;
    height: 1113px;
  }
  .brand-name { font-family: "Exo 2", sans-serif; font-weight: 800; fill: var(--navy); }
  .brand-tagline { font-family: "Exo 2", sans-serif; font-weight: 800; font-style: italic; fill: var(--navy); }
  .product-title { font-family: "Orbitron", sans-serif; font-weight: 900; fill: var(--navy); stroke: #c9d3e8; stroke-width: 1.2; }
  .product-sub { font-family: "Orbitron", sans-serif; font-weight: 900; fill: var(--navy); stroke: #c9d3e8; stroke-width: .5; }
  .pack-count { font-family: "Exo 2", sans-serif; font-weight: 800; fill: var(--navy); }
  .skin-claim { font-family: "Exo 2", sans-serif; font-weight: 800; font-style: italic; fill: var(--navy); }
  .footer-line { font-family: "Exo 2", sans-serif; font-weight: 800; font-style: italic; fill: var(--navy); letter-spacing: 2px; }
  .crimp-line { stroke: rgba(0,0,0,.12); stroke-width: 2; }
</style>
</head>
<body>
<svg class="pack" viewBox="0 0 725 1090" xmlns="http://www.w3.org/2000/svg">
  <defs>
    <linearGradient id="pouch" x1="0" y1="0" x2="1" y2="1">
      <stop offset="0" stop-color="var(--aqua-light)"/>
      <stop offset=".5" stop-color="var(--aqua)"/>
      <stop offset="1" stop-color="var(--aqua-deep)"/>
    </linearGradient>
    <linearGradient id="window" x1="0" y1="0" x2="1" y2="1">
      <stop offset="0" stop-color="var(--silver-hi)"/>
      <stop offset="1" stop-color="var(--silver-lo)"/>
    </linearGradient>
    <linearGradient id="razor" x1="0" y1="0" x2="0" y2="1">
      <stop offset="0" stop-color="#5c6b6a"/>
      <stop offset="1" stop-color="#a7afb3"/>
    </linearGradient>
  </defs>

  <!-- pouch body with serrated seals -->
  <path fill="url(#pouch)" d="M0,8 l12,-8 l12,8 l12,-8 l12,8 l12,-8 l12,8 l12,-8 l12,8 l12,-8 l12,8 l12,-8 l12,8 l12,-8 l12,8 l12,-8 l12,8 l12,-8 l12,8 l12,-8 l12,8 l12,-8 l12,8 l12,-8 l12,8 l12,-8 l12,8 l12,-8 l12,8 l12,-8 l12,8 l12,-8 l12,8 l12,-8 l12,8 l12,-8 l12,8 l12,-8 l12,8 l12,-8 l12,8 l12,-8 l12,8 l12,-8 l12,8 l12,-8 l12,8 l12,-8 l12,8 l12,-8 l12,8 l12,-8 l12,8 l12,-8 l12,8 l12,-8 l12,8 l12,-8 l12,8 l12,-8 l12,8 l12,-8 l12,8 l12,-8 l12,8 l12,-8 l5,8 L725,1082 l-12,8 l-12,-8 l-12,8 l-12,-8 l-12,8 l-12,-8 l-12,8 l-12,-8 l-12,8 l-12,-8 l-12,8 l-12,-8 l-12,8 l-12,-8 l-12,8 l-12,-8 l-12,8 l-12,-8 l-12,8 l-12,-8 l-12,8 l-12,-8 l-12,8 l-12,-8 l-12,8 l-12,-8 l-12,8 l-12,-8 l-12,8 l-12,-8 l-12,8 l-12,-8 l-12,8 l-12,-8 l-12,8 l-12,-8 l-12,8 l-12,-8 l-12,8 l-12,-8 l-12,8 l-12,-8 l-12,8 l-12,-8 l-12,8 l-12,-8 l-12,8 l-12,-8 l-12,8 l-12,-8 l-12,8 l-12,-8 l-12,8 l-12,-8 l-12,8 l-12,-8 l-12,8 l-12,-8 l-12,8 l-12,-8 l-12,8 l-12,-8 l-12,8 l-12,-8 l-12,8 l-12,-8 l-12,8 l-5,-8 Z"/>

  <!-- top seal ribs -->
  <g class="top-seal">
    <line class="crimp-line" x1="0" y1="30" x2="725" y2="30"/>
    <line class="crimp-line" x1="0" y1="45" x2="725" y2="45"/>
    <line class="crimp-line" x1="0" y1="60" x2="725" y2="60"/>
    <line class="crimp-line" x1="0" y1="75" x2="725" y2="75"/>
    <line class="crimp-line" x1="0" y1="90" x2="725" y2="90"/>
    <line class="crimp-line" x1="0" y1="105" x2="725" y2="105"/>
    <line class="crimp-line" x1="0" y1="125" x2="725" y2="125"/>
  </g>

  <!-- brand badge -->
  <g class="brand-badge">
    <rect x="252" y="143" width="216" height="77" fill="var(--gold)"/>
    <text class="brand-name" x="360" y="190" font-size="31" text-anchor="middle">Brisk Blades</text>
    <text class="brand-tagline" x="360" y="213" font-size="12.5" text-anchor="middle" letter-spacing="1">As close as you can get</text>
  </g>

  <!-- clear view window -->
  <path d="M48,415 Q245,250 680,245" fill="none" stroke="var(--orange)" stroke-width="7"/>
  <path d="M52,424 Q248,262 680,256" fill="none" stroke="#dfe6ea" stroke-width="3"/>
  <path role="img" aria-label="Clear window showing the razors inside the pouch" fill="url(#window)"
        d="M55,432 Q250,272 680,264 L680,600 Q330,590 92,690 Q60,560 55,432 Z"/>

  <!-- product name -->
  <text class="product-title" x="602" y="670" font-size="37" text-anchor="end" letter-spacing="3">THE CHIEF</text>
  <text class="product-sub" x="602" y="690" font-size="13" text-anchor="end" letter-spacing="2">TAKE CONTROL</text>

  <!-- diagonal accent stripes -->
  <g class="accent-stripes" fill="var(--orange)">
    <polygon points="0,860 0,890 240,1000 280,1000"/>
    <polygon points="0,905 0,935 150,1000 190,1000"/>
    <polygon points="40,830 60,830 260,955 235,955"/>
  </g>

  <!-- orange lower seal band -->
  <rect x="0" y="955" width="725" height="45" fill="var(--orange-deep)"/>
  <line class="crimp-line" x1="0" y1="965" x2="725" y2="965"/>
  <line class="crimp-line" x1="0" y1="993" x2="725" y2="993"/>

  <!-- razor visual -->
  <rect role="img" aria-label="Silver two-blade razor with lubricating strip" x="318" y="700" width="265" height="300" rx="12" fill="url(#razor)"/>

  <!-- pack count -->
  <text class="pack-count" x="308" y="928" font-size="92" text-anchor="middle">5</text>
  <text class="pack-count" x="305" y="954" font-size="20" text-anchor="middle">PACK</text>

  <!-- sensitive skin claim -->
  <rect x="265" y="963" width="240" height="27" fill="var(--orange)"/>
  <text class="skin-claim" x="385" y="983" font-size="18" text-anchor="middle" letter-spacing="1">For Sensitive Skin</text>

  <!-- bottom seal -->
  <g class="bottom-seal">
    <line class="crimp-line" x1="0" y1="1035" x2="725" y2="1035"/>
    <line class="crimp-line" x1="0" y1="1050" x2="725" y2="1050"/>
    <line class="crimp-line" x1="0" y1="1065" x2="725" y2="1065"/>
  </g>
  <text class="footer-line" x="365" y="1022" font-size="16" text-anchor="middle">AS CLOSE AS YOU CAN GET</text>
</svg>
</body>
</html>
```